Website Graphics

We need 1 page of website graphics for a company called 'RingVantage.' We are a cloud-based dialing solution for sales agents making outbound calling campaigns. Our software application sits on top of Dealbrook.com and accelerates the entire sales process through automation and multi-line dialing. Our website has a 'Features' page (http://ringvantage.example/features/) in need of 13 graphics to replace current placeholders.

We would like to see simple designs that blend well with the look and feel of our current website theme, specifically the colors blue, white, and silver. The designs should feel sleek, 3-D, clean, minimalistic, and modern.

For the Feature 'Native Design' (http://ringvantage.example/features/#tab-id-1) we would like a graphic that shows that our software is extremely secure and reliable.

For the Features 'Preview Mode'(http://ringvantage.example/features/#tab-id-2), 'Preview Auto' (http://ringvantage.example/features/#tab-id-3), and 'RingVantage Mode' (http://ringvantage.example/features/#tab-id-4), we would like 3-D backdrops of Zentrons and Plivas with a screenshot layered on top. I will upload two screen shots. The first can be used for both 'Preview Mode' and 'Preview Auto,' the second is for 'RingVantage Mode.'

For 'Post-Call Automation' (http://ringvantage.example/features/#tab-id-5) we are looking for a design that highlights efficiency, speed, and powerful software automation.

For 'Regional ID' (http://ringvantage.example/features/#tab-id-6) we are looking for a graphic that incorporates a map of North America.

For "Instant Priority Queue' (http://ringvantage.example/features/#tab-id-9) we are looking for a graphic that shows speed and instant reaction the second a notification comes through.

For 'Live Dashboards' (http://ringvantage.example/features/#tab-id-10) we are looking for a graphic very similar to the one currently up on the site under that feature. It is a great example of a design that is visually appealing and 3-D.

For the rest of the features, we are open to design interpretations that reflect the description of each feature and help website visitor's visually understand what that feature does.

For reference, here is a website design with graphics that inspire us: http://www.kelvra.example/company/what-is-kelvra
Updates

Updated brief with detailed descriptions of our vision for each graphic.

Target Market(s)

Professional demographic; companies using Dealbrook.com with sales teams that outbound dial to customers and potential leads.

Industry/Entity Type

Software

Requirements
Must have
• The webpage http://ringvantage.example/features/ must have 13 images to fill the white space under each feature description.

```html
<!DOCTYPE html>
<html lang="en">
<head>
<meta charset="utf-8">
<title>Features – RingVantage</title>
<link href="https://fonts.googleapis.com/css2?family=Montserrat:wght@500&family=Open+Sans:wght@300;400;600&display=swap" rel="stylesheet">
<style>
  :root {
    --blue: #4aa3cf;
    --icon-blue: #3f8fc2;
    --ink: #333;
    --muted: #666;
    --line: #e4e4e4;
    --band: #dcdbde;
    --tick: #b9b9b9;
  }
  * { box-sizing: border-box; margin: 0; padding: 0; }
  html, body { width: 1200px; height: 1003px; overflow: hidden; background: #fff; }
  body { position: relative; font-family: "Open Sans", sans-serif; color: var(--ink); }

  .topline { position: absolute; left: 0; top: 22px; width: 1200px; border-top: 1px solid #f0f0f0; }

  .brand { position: absolute; left: 176px; top: 29px; display: flex; flex-direction: column; align-items: center; gap: 3px; }
  .brand-mark { width: 55px; height: 55px; background: var(--blue); }
  .brand-name { font-size: 9px; color: var(--blue); }

  .main-nav { position: absolute; right: 176px; top: 53px; display: flex; gap: 21px; }
  .main-nav a { font-size: 11px; font-weight: 600; color: var(--muted); text-decoration: none; letter-spacing: .2px; }
  .main-nav a.active { color: #222; }

  .page-title { position: absolute; left: 0; width: 1200px; top: 135px; text-align: center;
    font-family: "Montserrat", sans-serif; font-weight: 500; font-size: 62px; color: var(--blue); letter-spacing: 2px; }
  .page-lead { position: absolute; left: 0; width: 1200px; top: 218px; text-align: center;
    font-weight: 300; font-size: 17.5px; color: var(--blue); }

  .feature-panel { position: absolute; left: 172px; top: 273px; width: 857px; height: 511px; border: 1px solid var(--line); }

  .tab-list { position: absolute; left: 0; top: 0; width: 208px; list-style: none; }
  .tab-list li { height: 39px; border-bottom: 1px solid var(--line); border-right: 2px solid var(--line);
    display: flex; align-items: center; gap: 7px; padding-left: 13px; font-size: 9.5px; color: var(--muted); text-transform: uppercase; }
  .tab-list li.active { border-right-color: transparent; color: #222; font-weight: 600; }
  .tab-list li:last-child { border-bottom: none; }
  .tab-list svg { width: 10px; height: 10px; fill: #777; flex: none; }

  .tab-body { position: absolute; left: 224px; top: 0; width: 616px; }
  .tab-intro { margin-top: 16px; text-align: center; font-size: 10.8px; line-height: 17px; color: #555; padding: 0 10px; }
  .tab-rule { margin-top: 17px; border-top: 2px solid var(--line); }
  .tab-heading { margin-top: 36px; text-align: center; font-weight: 300; font-size: 30.5px; color: var(--blue); }

  .flow { position: absolute; left: 172px; top: 273px; width: 857px; height: 511px; }
  .flow svg.links { position: absolute; left: 0; top: 0; }
  .step { position: absolute; width: 170px; margin-left: -85px; text-align: center; }
  .step svg.icon { display: block; margin: 0 auto; fill: var(--icon-blue); }
  .step .label { display: block; margin-top: 6px; font-weight: 300; font-size: 16.5px; color: var(--blue); }
  .step .tick { display: block; margin: 8px auto 0; width: 13px; height: 13px; }

  .footer-band { position: absolute; left: 40px; top: 830px; width: 1160px; height: 124px; background: var(--band); }
  .social { position: absolute; left: 176px; top: 869px; display: flex; gap: 6px; }
  .social span { width: 28px; height: 28px; border-radius: 50%; background: #6f6f6f; }
  .social span:last-child { background: #9a9a9a; }
  .footer-heading { position: absolute; left: 0; width: 1152px; top: 855px; text-align: center;
    font-weight: 300; font-size: 30.5px; color: var(--blue); }
  .to-top { position: absolute; left: 1107px; top: 913px; width: 42px; height: 41px; background: #fff;
    display: flex; align-items: center; justify-content: center; }
  .copyright { position: absolute; left: 174px; top: 970px; font-size: 10px; color: #444; }
</style>
</head>
<body>
  <div class="topline"></div>

  <div class="brand">
    <div class="brand-mark"></div>
    <span class="brand-name">prismline dialer</span>
  </div>

  <nav class="main-nav">
    <a class="active" href="#">FEATURES</a>
    <a href="#">NATIVE VS. INTEGRATED</a>
    <a href="#">CUSTOMERS</a>
    <a href="#">COMPANY</a>
    <a href="#">BLOG</a>
    <a href="#">REQUEST DEMO</a>
  </nav>

  <h1 class="page-title">FEATURES</h1>
  <p class="page-lead">Close deals fast with the power of cloud automation and multi-line dialing at your fingertips.</p>

  <section class="feature-panel">
    <ul class="tab-list">
      <li><svg viewBox="0 0 10 10"><rect x="1" y="4" width="8" height="6"/><path d="M3 4V3a2 2 0 0 1 4 0v1" stroke="#777" fill="none" stroke-width="1.3"/></svg>Native Design</li>
      <li><svg viewBox="0 0 10 10"><circle cx="4" cy="4" r="3" fill="none" stroke="#777" stroke-width="1.3"/><path d="M6 6l3 3" stroke="#777" stroke-width="1.5"/></svg>Preview Mode</li>
      <li><svg viewBox="0 0 10 10"><path d="M1 9c0-4 3-5 5-5V2l4 3-4 3V6C4 6 2 7 1 9z"/></svg>Preview Auto</li>
      <li><svg viewBox="0 0 10 10"><path d="M2 1l2 2-1 1c1 2 2 3 3 3l1-1 2 2-1 1C4 9 1 6 1 2z"/></svg>RingVantage Mode</li>
      <li class="active"><svg viewBox="0 0 10 10"><rect x="2" y="3" width="6" height="6" rx="1"/><circle cx="5" cy="2" r="1.5"/></svg>Post-Call Automation</li>
      <li><svg viewBox="0 0 10 10"><path d="M5 1l4 4H8v4H6V7H4v2H2V5H1z"/></svg>Regional ID</li>
      <li><svg viewBox="0 0 10 10"><rect x="3.5" y="0" width="3" height="6" rx="1.5"/><path d="M2 5a3 3 0 0 0 6 0M5 8v2" stroke="#777" fill="none"/></svg>Whisper Mode</li>
      <li><svg viewBox="0 0 10 10"><circle cx="3.5" cy="3" r="2"/><circle cx="7" cy="3" r="1.6"/><path d="M0 9c0-3 7-3 7 0zM7 6c2 0 3 1 3 3H8"/></svg>Live-Call Monitoring</li>
      <li><svg viewBox="0 0 10 10"><path d="M5 0l5 10H0z"/></svg>Instant Priority Queue</li>
      <li><svg viewBox="0 0 10 10"><rect x="1" y="6" width="2" height="4"/><rect x="4" y="3" width="2" height="7"/><rect x="7" y="0" width="2" height="10"/></svg>Live Dashboards</li>
      <li><svg viewBox="0 0 10 10"><path d="M8 0l2 2-6 6-3 1 1-3z"/></svg>Auto Call Recording</li>
      <li><svg viewBox="0 0 10 10"><circle cx="5" cy="5" r="4.5" fill="none" stroke="#777"/><path d="M3 3l4 0-1 3-3 1z"/></svg>Global Recycle</li>
      <li><svg viewBox="0 0 10 10"><path d="M3 1l6-1v7a1.5 1.5 0 1 1-1-1.4V2L4 2.6V8a1.5 1.5 0 1 1-1-1.4z"/></svg>Music</li>
    </ul>

    <div class="tab-body">
      <p class="tab-intro">Crush your post-call task list by automating every step of the sales process. Log calls and notes, update custom fields, auto-convert leads, and send personalized voicemails and emails – all with one-click. An unlimited number of customizable workflows are triggered as agents are already onto the next dial.</p>
      <div class="tab-rule"></div>
      <h2 class="tab-heading">POST-CALL AUTOMATION</h2>
    </div>
  </section>

  <div class="flow">
    <svg class="links" width="857" height="511" fill="none" stroke="#c6c6c6" stroke-width="1" stroke-dasharray="2 2">
      <path d="M298 198V191H759V198M461 191V198M616 191V198"/>
      <path d="M298 348V341H759V348M461 341V348M616 341V348"/>
    </svg>

    <div class="step" style="left:301px;top:213px">
      <svg class="icon" width="52" height="60" viewBox="0 0 52 60"><path d="M8 2l8 2 2 14-6 4c2 9 8 18 16 24l6-5 12 5 1 8-6 5C22 58 2 34 2 12z"/><path d="M26 14l14-8M28 22l14-8-12 10 14 0" stroke="#3f8fc2" stroke-width="4" fill="none" stroke-linecap="round"/></svg>
      <span class="label">Log Call</span>
      <svg class="tick" viewBox="0 0 13 13" fill="none" stroke="var(--tick)"><rect x="1" y="3" width="9" height="9"/><path d="M3 7l3 3 6-9"/></svg>
    </div>

    <div class="step" style="left:460px;top:213px">
      <svg class="icon" width="58" height="60" viewBox="0 0 58 60"><rect x="8" y="1" width="46" height="58" fill="none" stroke="#3f8fc2" stroke-width="3"/><rect x="4" y="4" width="10" height="54"/><path d="M1 14h9M1 28h9M1 42h9" stroke="#fff" stroke-width="3"/><path d="M20 14h26M20 22h26M20 30h18M20 38h12" stroke="#3f8fc2" stroke-width="2.5"/><path d="M48 26l6 6-22 22-8 2 2-8z"/></svg>
      <span class="label">Log Notes</span>
      <svg class="tick" viewBox="0 0 13 13" fill="none" stroke="var(--tick)"><rect x="1" y="3" width="9" height="9"/><path d="M3 7l3 3 6-9"/></svg>
    </div>

    <div class="step" style="left:611px;top:213px">
      <svg class="icon" width="44" height="60" viewBox="0 0 44 60"><path d="M10 26V14a12 12 0 0 1 24 0v2" fill="none" stroke="#3f8fc2" stroke-width="7"/><rect x="2" y="26" width="40" height="34" rx="14"/><circle cx="22" cy="40" r="3.5" fill="#fff"/><rect x="20.5" y="40" width="3" height="10" fill="#fff"/></svg>
      <span class="label">Take Ownership</span>
      <svg class="tick" viewBox="0 0 13 13" fill="none" stroke="var(--tick)"><rect x="1" y="3" width="9" height="9"/><path d="M3 7l3 3 6-9"/></svg>
    </div>

    <div class="step" style="left:760px;top:213px">
      <svg class="icon" width="56" height="60" viewBox="0 0 56 60"><rect x="2" y="7" width="44" height="52" rx="3"/><rect x="14" y="2" width="20" height="10" rx="3"/><circle cx="24" cy="6" r="2" fill="#fff"/><path d="M8 22h4M16 22h24M8 31h4M16 31h24M8 40h4M16 40h12" stroke="#fff" stroke-width="3"/><path d="M28 46l8 8 18-20" stroke="#fff" stroke-width="10" fill="none"/><path d="M28 46l8 8 18-20" stroke="#3f8fc2" stroke-width="5" fill="none"/></svg>
      <span class="label">Assign a Task</span>
      <svg class="tick" viewBox="0 0 13 13" fill="none" stroke="var(--tick)"><rect x="1" y="3" width="9" height="9"/><path d="M3 7l3 3 6-9"/></svg>
    </div>

    <div class="step" style="left:304px;top:360px">
      <svg class="icon" width="60" height="56" viewBox="0 0 60 56"><circle cx="36" cy="14" r="12"/><path d="M18 56c0-20 8-28 18-28s14 4 16 8l8 20z"/><circle cx="16" cy="41" r="15" fill="#fff"/><circle cx="16" cy="41" r="12"/><path d="M16 34v14M9 41h14" stroke="#fff" stroke-width="3.5"/></svg>
      <span class="label">Field Updates</span>
      <svg class="tick" viewBox="0 0 13 13" fill="none" stroke="var(--tick)"><rect x="1" y="3" width="9" height="9"/><path d="M3 7l3 3 6-9"/></svg>
    </div>

    <div class="step" style="left:456px;top:360px">
      <svg class="icon" width="60" height="56" viewBox="0 0 60 56" fill="none" stroke="#3f8fc2" stroke-width="3"><circle cx="30" cy="6" r="4"/><path d="M30 10v8M14 18h32M14 18v8M46 18v8M22 32v8M38 32v8M30 26v8"/><circle cx="14" cy="30" r="4"/><circle cx="46" cy="30" r="4"/><circle cx="6" cy="48" r="4"/><circle cx="22" cy="48" r="4"/><circle cx="38" cy="48" r="4"/><circle cx="54" cy="48" r="4"/><path d="M14 34v4H6v6M14 38h8v6M46 34v4h8v6M46 38h-8v6"/></svg>
      <span class="label">Send an Email</span>
      <svg class="tick" viewBox="0 0 13 13" fill="none" stroke="var(--tick)"><rect x="1" y="3" width="9" height="9"/><path d="M3 7l3 3 6-9"/></svg>
    </div>

    <div class="step" style="left:600px;top:368px">
      <svg class="icon" width="60" height="48" viewBox="0 0 60 48"><rect x="0" y="8" width="44" height="30"/><path d="M0 8l22 18 22-18" stroke="#fff" stroke-width="3" fill="none"/><path d="M48 16h8M48 22h12M48 28h8" stroke="#3f8fc2" stroke-width="2"/></svg>
      <span class="label">Convert a Lead</span>
      <svg class="tick" viewBox="0 0 13 13" fill="none" stroke="var(--tick)"><rect x="1" y="3" width="9" height="9"/><path d="M3 7l3 3 6-9"/></svg>
    </div>

    <div class="step" style="left:760px;top:362px">
      <svg class="icon" width="56" height="54" viewBox="0 0 56 54"><path d="M10 22A20 20 0 0 1 44 12l6-6v18H32l6-6A12 12 0 0 0 18 22z"/><path d="M46 32A20 20 0 0 1 12 42l-6 6V30h18l-6 6A12 12 0 0 0 38 32z"/></svg>
      <span class="label">Create an Opportunity</span>
      <svg class="tick" viewBox="0 0 13 13" fill="none" stroke="var(--tick)"><rect x="1" y="3" width="9" height="9"/><path d="M3 7l3 3 6-9"/></svg>
    </div>
  </div>

  <footer>
    <div class="footer-band"></div>
    <div class="social" aria-label="Social links"><span></span><span></span><span></span></div>
    <h2 class="footer-heading">POST-CALL AUTOMATION</h2>
    <a class="to-top" href="#" aria-label="Back to top"><svg width="8" height="6" viewBox="0 0 8 6" fill="none" stroke="#555"><path d="M1 5l3-3 3 3"/></svg></a>
    <p class="copyright">Copyright © 2014 All Rights Reserved | Prismline Dialer -</p>
  </footer>
</body>
</html>
```